Tandem Tots Flyer - 2 WEEK FREE TRIAL

FLYER - We need a 1 page DL flyer with images and text. Have flyer in landscape

OFFER - 2 WEEK FREE TRIAL

HOW TO GET
Book online now at www.tandemtotsplay.com.au/booking

TAG -Where Kids are Champions

PRIZE
Chance to win Full Term of 10 weekly sessions

GIVEAWAYS
Chance to get giveaways such as tickets to games, footballs or other great offers.

LOGO - Attached

Target Market(s)

Parents of children from 5 to 16

Industry/Entity Type

Fitness

Colors
0455a3
ffc214

Requirements
Must have
• Attraction for parents to go online and sign up their kids
Should not have
• Not dull or boring

```html
<!DOCTYPE html>
<html lang="en">
<head>
<meta charset="utf-8">
<title>Tandem Tots – 2 Week Free Trial Flyer</title>
<link rel="stylesheet" href="https://fonts.googleapis.com/css2?family=Jost:wght@400;500;600;700&display=swap">
<style>
  :root {
    --navy: #252f6d;
    --gold: #e9bf3b;
    --white: #ffffff;
    --backdrop: #c0bfbf;
    --fence: #b9d2c4;
    --net: #7fbf6a;
    --shirt: #f4661c;
    --shirt-soft: #f08a3a;
    --turf-light: #5fb03a;
    --turf: #2f8a22;
  }
  * { box-sizing: border-box; margin: 0; padding: 0; }
  html, body {
    width: 1200px; height: 900px; overflow: hidden;
    background: var(--backdrop);
    font-family: "Jost", "Futura", sans-serif;
  }
  .flyer {
    position: absolute; left: 205px; top: 248px;
    width: 781px; height: 389px;
    background: var(--navy);
    overflow: hidden;
  }
  .hero-photo {
    position: absolute; inset: 0;
    clip-path: polygon(352px 0, 781px 0, 781px 389px, 192px 389px);
    background: linear-gradient(180deg,
      var(--fence) 0%, var(--fence) 10%,
      var(--net) 20%, var(--turf-light) 27%,
      var(--shirt-soft) 37%, var(--shirt) 45%, var(--shirt) 55%,
      var(--shirt-soft) 61%, var(--turf-light) 70%,
      var(--turf) 100%);
  }
  .tagline-band {
    position: absolute; left: 340px; top: 0;
    width: 441px; height: 37px;
    background: var(--navy);
    display: flex; align-items: center; justify-content: flex-end;
    padding-right: 36px;
  }
  .tagline {
    color: var(--gold); font-weight: 700; font-size: 23px;
    letter-spacing: .9px; text-transform: uppercase;
  }
  .divider-stripe { position: absolute; inset: 0; pointer-events: none; }
  .brand {
    position: absolute; left: 40px; top: 24px; width: 150px;
    text-align: center;
    color: var(--gold); font-weight: 700; font-size: 29px;
    line-height: 1.05; text-transform: uppercase;
  }
  .brand-dot {
    display: block; width: 30px; height: 30px; margin: 0 auto 10px;
    border-radius: 50%; background: var(--gold);
  }
  .info { position: absolute; left: 14px; top: 164px; width: 200px; }
  .info-heading {
    color: var(--gold); font-weight: 500; font-size: 20px;
    text-transform: uppercase; line-height: 1.1;
  }
  .info-text { color: var(--white); font-size: 13.5px; line-height: 1.18; }
  .info-text.lead { font-size: 16px; margin-top: 5px; }
  .info-url { color: var(--white); font-size: 13.5px; margin-top: 1px; white-space: nowrap; }
  .how-to-get { margin-bottom: 10px; }
  .prize { margin-bottom: 10px; }
  .prize .info-text, .giveaways .info-text { margin-top: 5px; }
  .offer-badge { position: absolute; left: 173px; top: 240px; width: 102px; height: 96px; }
</style>
</head>
<body>
  <main class="flyer">
    <div class="hero-photo" role="img" aria-label="Four smiling children in orange jerseys lying on green turf in front of a goal net, holding a gold trophy and a soccer ball"></div>

    <header class="tagline-band">
      <h1 class="tagline">Where Kids Are Champions</h1>
    </header>

    <svg class="divider-stripe" width="781" height="389" viewBox="0 0 781 389" aria-hidden="true">
      <polygon points="337,0 353,0 193,389 177,389" fill="var(--gold)"/>
    </svg>

    <div class="brand">
      <span class="brand-dot"></span>
      Tandem Tots
    </div>

    <section class="info">
      <div class="how-to-get">
        <h2 class="info-heading">How to get</h2>
        <p class="info-text lead">Book online now at</p>
        <p class="info-url">www.tandemtotsplay.com.au/booking</p>
      </div>
      <div class="prize">
        <h2 class="info-heading">Prize</h2>
        <p class="info-text">Chance to win Full Term of<br>10 weekly sessions</p>
      </div>
      <div class="giveaways">
        <h2 class="info-heading">Giveaways</h2>
        <p class="info-text">Chance to get giveaways such<br>as tickets to games, footballs<br>or other great offers.</p>
      </div>
    </section>

    <svg class="offer-badge" viewBox="0 0 102 96" aria-label="Offer: free trial, 2 week">
      <path d="M14 4 H88 L92 10 V58 C92 74 70 86 51 93 C32 86 10 74 10 58 V10 Z" fill="var(--navy)" stroke="var(--gold)" stroke-width="3"/>
      <text x="51" y="22" text-anchor="middle" fill="var(--white)" font-family="Jost, sans-serif" font-weight="700" font-size="15">OFFER</text>
      <path d="M0 28 H102 L96 39 L102 50 H0 L6 39 Z" fill="var(--gold)"/>
      <text x="51" y="45" text-anchor="middle" fill="var(--white)" font-family="Jost, sans-serif" font-weight="500" font-size="16">FREE TRIAL</text>
      <text x="51" y="67" text-anchor="middle" fill="var(--white)" font-family="Jost, sans-serif" font-weight="500" font-size="14">2 WEEK</text>
      <g fill="var(--gold)">
        <circle cx="36" cy="77" r="1.6"/><circle cx="43" cy="80" r="1.6"/>
        <circle cx="51" cy="82" r="2"/><circle cx="59" cy="80" r="1.6"/><circle cx="66" cy="77" r="1.6"/>
      </g>
    </svg>
  </main>
</body>
</html>
```